Cutting Edge Cloud Hosting Provider needs business card design

We are a new Cloud Hosting Provider called Verdalo Hosting. (Verdalo means cloudy in Spanish.) We provide clients with virtual resources and not virtual machines directly. Our clients purchase the resources that they will use (RAM,CPU, Hard drive space) then use those resources in as many virtual machines as they like.

We are looking for a business card design that is cutting edge and hip.
Updates

The name of the company is "Verdalo Hosting". Please include the "Hosting" part of our name in the design.

Thanks

Target Market(s)

21-35 developers and I.T. Staff

Industry/Entity Type

Business

Requirements
Must have
• Rounded corners, Must Incorporate our logo, individual's name must be prominent

```html
<!DOCTYPE html>
<html lang="en">
<head>
<meta charset="utf-8">
<title>Verdalo Hosting – Business Card</title>
<link rel="stylesheet" href="https://fonts.googleapis.com/css2?family=Quicksand:wght@500&family=Tinos&display=swap">
<style>
  :root {
    --backdrop: #95663a;
    --card: #f4f8fd;
    --navy: #1a3a6b;
    --sky: #6cb4e4;
    --sky-line: #7fb8e2;
  }
  * { margin: 0; padding: 0; box-sizing: border-box; }
  html, body {
    width: 1100px; height: 1200px; overflow: hidden;
    background: var(--backdrop);
  }
  .canvas { position: relative; width: 1100px; height: 1200px; }
  .card {
    position: absolute;
    background: var(--card);
    border-radius: 58px;
  }
  .card--front { left: 36px; top: 43px; width: 1027px; height: 520px; }
  .card--back  { left: 39px; top: 633px; width: 1024px; height: 519px; }
  .t { position: absolute; line-height: 1; white-space: nowrap; color: var(--navy); }
  .brand { font-family: "Quicksand", sans-serif; font-weight: 500; }
  .serif { font-family: "Tinos", serif; }

  .front-brand { left: 22px; top: 30px; font-size: 62px; }
  .front-brand-sub { left: 247px; top: 128px; font-size: 42px; }
  .contact { left: 682px; font-size: 33px; }
  .contact--cell { top: 20px; }
  .contact--phone { top: 63px; }
  .holder-name { left: 214px; top: 230px; font-size: 101px; }
  .rule { position: absolute; height: 2px; }
  .rule--name { left: 202px; top: 325px; width: 588px; background: var(--sky-line); }
  .rule--title { left: 686px; top: 334px; width: 130px; background: var(--navy); height: 3px; }
  .holder-title { left: 716px; top: 348px; font-size: 52px; color: var(--sky); }
  .email { left: 19px; top: 446px; font-size: 46px; }

  .back-brand { left: 135px; top: 130px; font-size: 160px; }
  .back-brand-sub { left: 569px; top: 290px; font-size: 100px; }
  .website { left: 283px; top: 468px; font-size: 44px; }
</style>
</head>
<body>
<main class="canvas">
  <section class="card card--front" aria-label="Card front">
    <div class="t brand front-brand">Verdalo</div>
    <div class="t brand front-brand-sub">Hosting</div>
    <div class="t serif contact contact--cell">Cell: 555-014-2291</div>
    <div class="t serif contact contact--phone">Phone: 555-016-7730</div>
    <h1 class="t serif holder-name" style="font-weight:400">Marco Ibarra</h1>
    <div class="rule rule--name"></div>
    <div class="rule rule--title"></div>
    <div class="t brand holder-title">V.P.</div>
    <div class="t brand email">marco@verdalo.com</div>
  </section>

  <section class="card card--back" aria-label="Card back">
    <div class="t brand back-brand">Verdalo</div>
    <div class="t brand back-brand-sub">Hosting</div>
    <div class="t brand website">www.verdalo.net</div>
  </section>
</main>
</body>
</html>
```